Awesome Business Card Design needed!

Hey there.
I'm looking for a simple but awesome business card design.
Type of company: Online advertisement agency
(please don't use the typical business people or statistics images on the card)
The front has to display the business name
and possibly some sort of logo ( perhaps something with the two M's of the biz name )
And the back of the card should say:
Name
Phone
Email
Let your imagination flow.
here are some designs that I like and that you can use as inspiration.
Simple but Awesome
http://images.pixelvantor.net/designs/55128_877673_43091_thumbnail.jpg
http://images.pixelvantor.net/designs/37714_747642_40106_image.jpg
http://images.pixelvantor.net/designs/55128_877673_43091_image.jpg
http://images.pixelvantor.net/designs/51321_781878_43091_image.jpg
http://images.pixelvantor.net/designs/33378_399063_15912_image.jpg
http://images.pixelvantor.net/designs/2337_271604_9495_image.jpg
good luck

```html
<!DOCTYPE html>
<html lang="en">
<head>
<meta charset="utf-8">
<title>Veltrona Media – Business Card</title>
<link rel="stylesheet" href="https://fonts.googleapis.com/css2?family=Fira+Sans:wght@400;600&display=swap">
<style>
  :root {
    --stage-top: #121313;
    --stage-mid: #4a4e4e;
    --stage-bottom: #f2f2f2;
    --card: #0d0e0e;
    --card-edge: #1d1f1f;
    --card-glow: #181a1a;
    --ink: #ffffff;
    --accent: #5fd8d0;
    --brand: #c9cccc;
  }
  * { margin: 0; padding: 0; box-sizing: border-box; }
  html, body {
    width: 1200px;
    height: 1200px;
    overflow: hidden;
  }
  body {
    position: relative;
    background: linear-gradient(180deg, var(--stage-top) 0%, var(--stage-mid) 45%, var(--stage-bottom) 100%);
    font-family: "Fira Sans", Arial, sans-serif;
  }
  .card {
    position: absolute;
    background: var(--card);
    border: 1px solid var(--card-edge);
    box-shadow: 0 6px 14px rgba(0, 0, 0, 0.55);
    color: var(--ink);
    text-align: center;
  }
  /* Back of card: contact details */
  .card-back {
    left: 593px;
    top: 95px;
    width: 533px;
    height: 305px;
    background: linear-gradient(180deg, var(--card-glow) 0%, var(--card) 35%, var(--card) 100%);
  }
  .card-back .brand-name {
    position: absolute;
    top: 128px;
    left: 0;
    right: 0;
    margin-top: -14px;
    top: 120px;
  }
  .brand-name {
    color: var(--brand);
    font-weight: 600;
    letter-spacing: 0.5px;
  }
  .card-back .brand-name {
    top: 124px;
    font-size: 30px;
    top: 112px;
  }
  .tagline {
    position: absolute;
    top: 74px;
    left: 0;
    right: 0;
    font-size: 13px;
    color: var(--accent);
  }
  .card-back .brand-name { top: 30px; }
  .contact {
    position: absolute;
    top: 164px;
    left: 0;
    right: 0;
    font-size: 19px;
    line-height: 26px;
  }
  /* Front of card: business name */
  .card-front {
    left: 57px;
    top: 442px;
    width: 673px;
    height: 385px;
    background: radial-gradient(ellipse at 50% 40%, #1a1c1c 0%, var(--card) 70%);
  }
  .front-mark {
    position: absolute;
    left: 0;
    right: 0;
    top: 160px;
    display: flex;
    align-items: center;
    justify-content: center;
    gap: 18px;
  }
  .front-mark .square {
    width: 34px;
    height: 34px;
    background: var(--brand);
  }
  .card-front .brand-name {
    font-size: 46px;
    line-height: 1;
  }
</style>
</head>
<body>
  <section class="card card-back" aria-label="Business card back">
    <div class="brand-name">Veltrona Media</div>
    <div class="tagline">online advertisement agency</div>
    <div class="contact">
      <div class="contact-name">Daniel Harlow</div>
      <div class="contact-phone">phone: 00385 1 555014</div>
      <div class="contact-email">daniel@veltrona.com</div>
    </div>
  </section>

  <section class="card card-front" aria-label="Business card front">
    <div class="front-mark">
      <span class="square"></span>
      <span class="brand-name">Veltrona Media</span>
    </div>
  </section>
</body>
</html>
```